Website redesign and new logo

Hi we feel that the colours, layout and style along with the logo which is only text at the moment is poor. It seems to lack a quality and luxurious feel and we are about selling high end curtains. The text logo is hard to read as well in my opinion. We are looking for a overall revamp and an new logo. We want to maintain the main parts of the home page but happy to consider any ideas that will improve web traffic. It does not really reflect our achievements either of having curtains recently featured on Horizon 7 tv.
The website in question is www.lunaviewinteriors.co.uk

```html
<!DOCTYPE html>
<html lang="en">
<head>
<meta charset="utf-8">
<title>Lunaview Interiors – Home</title>
<link rel="stylesheet" href="https://fonts.googleapis.com/css2?family=Noto+Serif:ital,wght@0,400;1,400&display=swap">
<style>
  :root {
    --brand-red: #b8100f;
    --brand-red-dark: #8e0a0a;
    --band-red: #c01613;
    --nav-bg: #f2f2f2;
    --nav-divider: #dcdcdc;
    --ink: #2a2a2a;
    --white: #ffffff;
    --caption-dark: rgba(34, 32, 30, 0.86);
    --caption-light: rgba(255, 255, 255, 0.88);
    --rule-grey: #e6e6e6;
  }
  * { box-sizing: border-box; margin: 0; padding: 0; }
  html, body { width: 1200px; height: 914px; overflow: hidden; background: var(--white); }
  body { font-family: "Noto Serif", Georgia, serif; color: var(--ink); }
  .page { position: relative; width: 1200px; height: 914px; overflow: hidden; }

  /* Header / brand */
  .site-header { position: absolute; top: 0; left: 0; width: 1200px; height: 134px; }
  .brand { position: absolute; top: 14px; left: 0; width: 1200px; text-align: center; text-decoration: none; }
  .brand-mark { display: block; margin: 0 auto; width: 76px; height: 76px; border-radius: 50%; background: var(--brand-red); }
  .brand-name { display: block; margin-top: 9px; font-size: 16px; line-height: 20px; font-weight: 400; color: var(--brand-red); letter-spacing: 0.3px; }

  /* Navigation */
  .main-nav { position: absolute; top: 134px; left: 0; width: 1200px; height: 52px; background: var(--nav-bg); }
  .main-nav ul { list-style: none; position: absolute; left: 134px; top: 0; height: 52px; display: flex; }
  .main-nav li { position: relative; height: 52px; }
  .main-nav li + li::before { content: ""; position: absolute; left: 0; top: 8px; height: 34px; width: 1px; background: var(--nav-divider); }
  .main-nav a { display: block; height: 52px; line-height: 56px; text-align: center; font-style: italic; font-size: 14px; color: var(--ink); text-decoration: none; }
  .main-nav .is-current a { border-bottom: 3px solid var(--brand-red); }

  /* Hero */
  .hero { position: absolute; top: 186px; left: 0; width: 1200px; height: 375px;
    background:
      linear-gradient(180deg, rgba(255,255,255,0) 55%, rgba(235,225,215,0.55) 80%, rgba(200,185,170,0.6) 100%),
      radial-gradient(ellipse 260px 200px at 560px 150px, rgba(235,242,238,0.95), rgba(235,242,238,0) 100%),
      linear-gradient(90deg, #b8aa98 0%, #d8cdbd 10%, #efe6d8 22%, #e2d6c3 33%, #dfe4dc 42%, #c9d2c2 52%, #dcdfd6 62%, #ebe0d0 70%, #c9ab98 82%, #b99886 92%, #d9c6b6 100%); }
  .hero-title { position: absolute; left: 743px; top: 226px; width: 338px; height: 55px; background: var(--caption-dark);
    color: var(--white); font-style: italic; font-size: 32px; line-height: 55px; text-align: center; font-weight: 400; }
  .hero-tagline { position: absolute; left: 828px; top: 291px; width: 253px; height: 41px; background: var(--caption-light);
    color: var(--ink); font-style: italic; font-size: 18.5px; line-height: 41px; text-align: center; font-weight: 400; }

  /* Feature band */
  .feature-band { position: absolute; top: 561px; left: 0; width: 1200px; height: 294px;
    background: radial-gradient(ellipse 800px 260px at 600px 147px, #c41a16, var(--brand-red) 70%, #a90e0d 100%);
    border-bottom: 3px solid var(--brand-red-dark); }
  .gallery-panel { position: absolute; left: 121px; top: 28px; width: 960px; height: 234px; background: var(--white); }
  .section-title { position: absolute; left: 37px; top: 24px; font-size: 19px; line-height: 26px; font-style: italic; font-weight: 400; color: var(--ink); }
  .section-rule { position: absolute; left: 110px; top: 35px; width: 811px; height: 3px; background: var(--rule-grey); }
  .section-rule::before { content: ""; position: absolute; left: 0; top: 0; width: 19px; height: 3px; background: var(--brand-red); }
  .gallery-grid { position: absolute; left: 37px; top: 65px; display: flex; gap: 7px; list-style: none; }
  .gallery-item { width: 216px; height: 141px; }
  .gallery-item.drapes-leaf { background:
      linear-gradient(90deg, rgba(60,56,52,0.55) 0%, rgba(60,56,52,0) 30%),
      linear-gradient(180deg, #b9b0a5 0%, #a89f94 55%, #6f6862 100%); }
  .gallery-item.cushions-orange { background:
      linear-gradient(160deg, #e7e1d8 0%, #d8cfc4 30%, #ee7a42 45%, #f2935c 70%, #cfcbd2 88%, #b9b7c0 100%); }
  .gallery-item.drapes-diamond { background:
      linear-gradient(90deg, #8c8272 0%, #a49a88 25%, #5c5650 45%, #bdb6aa 52%, #4a4743 62%, #c9c2b6 72%, #57534d 82%, #9e978b 100%); }
  .gallery-item.cushions-teal { background:
      linear-gradient(150deg, #3e4c50 0%, #6f8b8e 35%, #8fa9aa 55%, #5a7074 75%, #33403f 100%); }

  /* Footer */
  .site-footer { position: absolute; top: 858px; left: 0; width: 1200px; height: 56px; background: var(--white); border-bottom: 2px solid var(--brand-red); }
  .copyright { position: absolute; left: 122px; top: 17px; font-size: 13px; font-style: italic; color: var(--ink); }
  .copyright .company { color: var(--brand-red); }
  .social-links { position: absolute; left: 1003px; top: 16px; display: flex; gap: 8px; list-style: none; }
  .social-links a { display: block; width: 20px; height: 20px; border-radius: 50%; background: #1a1a1a; }
</style>
</head>
<body>
<div class="page">
  <header class="site-header">
    <a class="brand" href="#">
      <span class="brand-mark" aria-hidden="true"></span>
      <span class="brand-name">Lunaview Interiors</span>
    </a>
  </header>

  <nav class="main-nav" aria-label="Main">
    <ul>
      <li class="is-current" style="width:85px"><a href="#">Home</a></li>
      <li style="width:103px"><a href="#">About Us</a></li>
      <li style="width:78px"><a href="#">News</a></li>
      <li style="width:92px"><a href="#">Fabrics</a></li>
      <li style="width:242px"><a href="#">Scatter Cushions &amp; Bed Throws</a></li>
      <li style="width:92px"><a href="#">Gallery</a></li>
      <li style="width:126px"><a href="#">Testimonials</a></li>
      <li style="width:112px"><a href="#">Contact Us</a></li>
    </ul>
  </nav>

  <section class="hero" role="img" aria-label="Bright bedroom with cream draped curtains framing a large window">
    <h1 class="hero-title">Homemade Curtain</h1>
    <p class="hero-tagline">find the luxury at home</p>
  </section>

  <section class="feature-band" aria-label="Gallery">
    <div class="gallery-panel">
      <span class="section-rule"></span>
      <h2 class="section-title">Gallery</h2>
      <ul class="gallery-grid">
        <li class="gallery-item drapes-leaf" role="img" aria-label="Grey leaf-pattern curtains beside an armchair"></li>
        <li class="gallery-item cushions-orange" role="img" aria-label="Orange and cream scatter cushions"></li>
        <li class="gallery-item drapes-diamond" role="img" aria-label="Black and white diamond-pattern curtains in a loft room"></li>
        <li class="gallery-item cushions-teal" role="img" aria-label="Teal patterned cushions close-up"></li>
      </ul>
    </div>
  </section>

  <footer class="site-footer">
    <p class="copyright">© Copyright <span class="company">Lunaview Interiors</span> 2013</p>
    <ul class="social-links">
      <li><a href="#" aria-label="Social profile 1"></a></li>
      <li><a href="#" aria-label="Social profile 2"></a></li>
      <li><a href="#" aria-label="Social profile 3"></a></li>
    </ul>
  </footer>
</div>
</body>
</html>
```